New Business Card for Web Design/Internet Marketing Company

Looking for a great looking new business card. We are a 10 year old web design, internet marketing and website management company that works mostly with small businesses.

Our new card needs to better match the colors and style of our website, be bold, extremely usable and slightly edgy.

Target Market(s)

Small/Medium businesses that have websites

Industry/Entity Type

Internet

Requirements
Must have
• Front and back design, full color, rounded corners please

Must use the colors/style of our website (JPG provided)

INFO FOR CARDS (as readable as possible please)
Mark Tilden
President/CEO
mark@brivatnet.example
Phone: 520-318-7051
Toll Free: 866-318-7051
Address: 4125 W. Larkspur Ave. Ste. 160, Tucson, AZ 85799

THINGS I WANT TO PROMOTE (if there is room):
1. Our Website - www.brivatnet.example

2. Social Media
Twitter: @brivatnet
Facebook: www.facebook.com/brivatnet

3. Our Services
Web Design
Internet Marketing
Website Management

```html
<!DOCTYPE html>
<html lang="en">
<head>
<meta charset="utf-8">
<title>Brivatnet Business Card</title>
<link href="https://fonts.googleapis.com/css2?family=Cabin:ital,wght@0,400;0,600;0,700;1,500&display=swap" rel="stylesheet">
<style>
  :root {
    --page-bg: #eceae6;
    --card-white: #ffffff;
    --brand-orange: #f47c20;
    --brand-blue: #0a7cc4;
    --blue-deep: #0447a0;
    --blue-light: #13a6e6;
    --ink: #2b2b2b;
    --muted: #6b6b6b;
  }
  * { margin: 0; padding: 0; box-sizing: border-box; }
  html, body {
    width: 1200px; height: 900px; overflow: hidden;
    background: var(--page-bg);
    font-family: "Cabin", sans-serif;
  }
  .sheet { position: relative; width: 1200px; height: 900px; }
  .card {
    position: absolute; left: 315px; width: 542px; height: 330px;
    border-radius: 20px; overflow: hidden;
    box-shadow: 0 6px 16px rgba(0,0,0,0.18);
  }
  /* Front */
  .card-front { top: 92px; background: var(--card-white); }
  .front-brand {
    position: absolute; left: 44px; top: 30px;
    display: flex; flex-direction: column; align-items: flex-end;
  }
  .brand-row { display: flex; align-items: center; gap: 12px; }
  .brand-dot {
    width: 34px; height: 34px; border-radius: 50%;
    background: var(--brand-blue);
  }
  .brand-name {
    font-size: 50px; font-weight: 700; line-height: 1;
    color: var(--brand-orange); letter-spacing: -0.5px;
  }
  .tagline { font-size: 15px; color: var(--muted); margin-top: 4px; }
  .contact {
    position: absolute; left: 44px; top: 132px;
    color: var(--ink); font-size: 15px; line-height: 19.5px;
  }
  .contact .person {
    color: var(--brand-orange); font-weight: 700; font-size: 17px; line-height: 21px;
  }
  .contact .role { margin-bottom: 12px; }
  .contact .label { color: var(--brand-orange); font-weight: 600; }
  .web-band {
    position: absolute; left: 0; right: 0; bottom: 0; height: 44px;
    background: linear-gradient(90deg, var(--brand-blue), var(--blue-light));
    display: flex; align-items: center; justify-content: center;
    color: #fff; font-style: italic; font-weight: 500; font-size: 19px; letter-spacing: 0.3px;
  }
  /* Back */
  .card-back {
    top: 459px;
    background: radial-gradient(ellipse at 50% 40%, var(--blue-light) 0%, #0a86d4 35%, var(--blue-deep) 100%);
  }
  .back-brand {
    position: absolute; left: 0; right: 0; top: 104px;
    display: flex; flex-direction: column; align-items: center;
  }
  .back-brand .brand-dot { background: var(--brand-orange); width: 38px; height: 38px; }
  .back-brand .brand-name { color: #fff; font-size: 58px; }
  .back-brand .tagline { color: #fff; margin-top: 10px; }
  .services {
    position: absolute; left: 0; right: 0; bottom: 26px;
    display: flex; justify-content: center; align-items: center; gap: 14px;
    color: #fff; font-size: 17px; letter-spacing: 0.4px;
  }
  .services .bullet {
    width: 7px; height: 7px; border-radius: 50%; background: var(--brand-orange);
  }
</style>
</head>
<body>
<main class="sheet">
  <section class="card card-front" aria-label="Card front">
    <div class="front-brand">
      <div class="brand-row">
        <span class="brand-dot"></span>
        <span class="brand-name">Brivatnet</span>
      </div>
      <p class="tagline">Sites that Work</p>
    </div>
    <div class="contact">
      <p class="person">Dana Korvell</p>
      <p class="role">President/CEO</p>
      <p>dana@brivatnet.example</p>
      <p><span class="label">P:</span> 520-318-7051</p>
      <p><span class="label">Toll Free:</span> 866-318-7051</p>
      <p><span class="label">A:</span> 4125 W. Larkspur Ave. Ste. 160,</p>
      <p>Tucson, AZ 85799</p>
    </div>
    <div class="web-band">www.brivatnet.example</div>
  </section>

  <section class="card card-back" aria-label="Card back">
    <div class="back-brand">
      <div class="brand-row">
        <span class="brand-dot"></span>
        <span class="brand-name">Brivatnet</span>
      </div>
      <p class="tagline">Sites that Work</p>
    </div>
    <div class="services">
      <span>Web Design</span><span class="bullet"></span>
      <span>Internet Marketing</span><span class="bullet"></span>
      <span>Website Management</span>
    </div>
  </section>
</main>
</body>
</html>
```